Business Card

Harbourline Athletics ([url removed, login to view]) develops fundraising software for not for profit sporting clubs/teams.

We launched only 12 months ago and ran limited beta testing software to ensure the quality of the software. Coming into the 2018 winter season we are ready to ramp it up.

As we are a new company the business card will need to show that we are trustworthy, a serious business and larger than we look. I am also looking for consistency within the brand.

The major fundraising software we will be running next year will be Lantern Play ([url removed, login to view]) which is a Tipping Competition for a number of sporting leagues in Australia.

Harbourline Athletics is the name of the company that should be the major focus but there should also be a secondary focus on Lantern Play (both logos are attached). I am happy to see suggestions of how this can work, either front and back differences or a combination, I am looking for suggestions from you.

I am thinking of a secondary catch line for Harbourline Athletics which is "Fundraising Software for Grass Roots Sport" which I would like to see incorporated.

Please add the following information (happy to see icons or other ways to display this info)

Name: Doug Pranley
Mobile: 0455 218 634 (i will give the number to the winner)
email: doug@[url removed, login to view]
Linked In - [url removed, login to view]
Web - [url removed, login to view]

If it works also having [url removed, login to view]

```html
<!DOCTYPE html>
<html lang="en">
<head>
<meta charset="utf-8">
<title>Harbourline Athletics – Business Card</title>
<link rel="stylesheet" href="https://fonts.googleapis.com/css2?family=Lato:wght@400;700;900&display=swap">
<style>
  :root {
    --stage: #3a3b3d;
    --brand-blue: #25489a;
    --brand-blue-deep: #1c3a82;
    --brand-green: #8cc63f;
    --ink: #2b2b2b;
    --ink-soft: #555a60;
    --paper: #ffffff;
    --paper-shade: #eef0f2;
    --lantern-red: #c8262c;
  }
  * { margin: 0; padding: 0; box-sizing: border-box; }
  html, body {
    width: 1200px; height: 900px; overflow: hidden;
    background: var(--stage);
    font-family: "Lato", Arial, sans-serif;
  }
  .card {
    position: absolute;
    left: 280px;
    width: 640px; height: 366px;
    overflow: hidden;
    box-shadow: 0 10px 24px rgba(0,0,0,.35);
  }
  /* front */
  .card-front {
    top: 70px;
    background: radial-gradient(ellipse at 45% 40%, #2f56a8 0%, var(--brand-blue) 45%, var(--brand-blue-deep) 100%);
    color: var(--paper);
  }
  .front-brand {
    position: absolute; left: 0; right: 0; top: 130px;
    display: flex; justify-content: center; align-items: center; gap: 14px;
  }
  .brand-square {
    width: 52px; height: 52px; background: var(--brand-green); flex: none;
  }
  .brand-text { display: flex; flex-direction: column; }
  .brand-name {
    font-weight: 900; font-size: 34px; line-height: 1; letter-spacing: -.3px;
    white-space: nowrap;
  }
  .front-brand .brand-name { color: var(--paper); }
  .brand-tagline {
    font-weight: 700; font-size: 15px; color: var(--brand-green); margin-top: 4px;
    white-space: nowrap;
  }
  .front-web {
    position: absolute; left: 0; right: 0; top: 268px;
    text-align: center; font-size: 14px; color: var(--paper);
  }

  /* back */
  .card-back {
    top: 464px;
    background: linear-gradient(160deg, var(--paper) 0%, var(--paper) 55%, var(--paper-shade) 100%);
    color: var(--ink);
  }
  .back-brand {
    position: absolute; right: 30px; top: 34px;
    display: flex; align-items: center; gap: 10px;
  }
  .back-brand .brand-square { width: 34px; height: 34px; }
  .back-brand .brand-name { font-size: 24px; color: var(--brand-blue); }
  .back-brand .brand-tagline { font-size: 11px; margin-top: 2px; }

  .partner-brand {
    position: absolute; left: 30px; top: 118px;
    display: flex; align-items: center; gap: 8px;
  }
  .partner-circle {
    width: 26px; height: 26px; border-radius: 50%; background: var(--lantern-red); flex: none;
  }
  .partner-text { display: flex; flex-direction: column; }
  .partner-name {
    font-weight: 900; font-size: 17px; color: var(--ink-soft);
    text-transform: uppercase; letter-spacing: .5px; line-height: 1;
  }
  .partner-web { font-size: 8px; color: var(--ink-soft); margin-top: 2px; }

  .rule {
    position: absolute; left: 200px; right: 22px; top: 110px;
    height: 2px; background: var(--brand-blue);
  }

  .person { position: absolute; left: 30px; top: 190px; }
  .person-name {
    font-weight: 700; font-size: 24px; color: var(--brand-blue);
    text-transform: uppercase; letter-spacing: .3px;
  }
  .person-role { font-weight: 700; font-size: 14px; color: var(--ink); margin-top: 2px; }

  .contact-list {
    position: absolute; left: 30px; top: 258px;
    list-style: none; font-size: 13px; color: var(--ink);
  }
  .contact-list li { display: flex; align-items: center; gap: 8px; height: 20px; }
  .contact-icon { width: 12px; height: 12px; flex: none; }

  .web-list {
    position: absolute; right: 24px; top: 236px;
    text-align: right; font-size: 13px; color: var(--ink); line-height: 18px;
  }

  .footer-bands { position: absolute; left: 0; bottom: 0; width: 640px; height: 90px; }
</style>
</head>
<body>

<section class="card card-front" aria-label="Card front">
  <div class="front-brand">
    <span class="brand-square"></span>
    <div class="brand-text">
      <span class="brand-name">Harbourline Athletics</span>
      <span class="brand-tagline">backing local clubs</span>
    </div>
  </div>
  <p class="front-web">www.harbourlineathletics.com</p>
</section>

<section class="card card-back" aria-label="Card back">
  <div class="back-brand">
    <span class="brand-square"></span>
    <div class="brand-text">
      <span class="brand-name">Harbourline Athletics</span>
      <span class="brand-tagline">backing local clubs</span>
    </div>
  </div>

  <div class="rule"></div>

  <div class="partner-brand">
    <span class="partner-circle"></span>
    <div class="partner-text">
      <span class="partner-name">Lantern Play</span>
      <span class="partner-web">www.lanternplay.com</span>
    </div>
  </div>

  <div class="person">
    <h1 class="person-name">Doug Pranley</h1>
    <p class="person-role">President &amp; CEO</p>
  </div>

  <ul class="contact-list">
    <li>
      <svg class="contact-icon" viewBox="0 0 12 12" aria-hidden="true">
        <path d="M2.5 1 L4.5 1 L5.2 3.4 L4 4.4 Q5 6.8 7.6 8 L8.6 6.8 L11 7.5 L11 9.5 Q10.5 11 9 11 Q1 10 1 2.6 Q1 1 2.5 1Z" fill="var(--brand-blue)"/>
      </svg>
      <span>0455 218 634</span>
    </li>
    <li>
      <svg class="contact-icon" viewBox="0 0 12 12" aria-hidden="true">
        <rect x="0.5" y="2" width="11" height="8" fill="var(--brand-blue)"/>
        <path d="M1 2.5 L6 6.5 L11 2.5" stroke="#fff" stroke-width="1" fill="none"/>
      </svg>
      <span>doug@harbourlineathletics.com</span>
    </li>
    <li>
      <svg class="contact-icon" viewBox="0 0 12 12" aria-hidden="true">
        <rect x="1" y="1" width="10" height="10" fill="var(--brand-blue)"/>
      </svg>
      <span>profilenet.io/in/dougpranley</span>
    </li>
  </ul>

  <div class="web-list">
    <p>www.harbourlineathletics.com</p>
    <p>www.lanternplay.com</p>
  </div>

  <svg class="footer-bands" viewBox="0 0 640 90" aria-hidden="true">
    <path d="M390 90 C410 40 430 34 470 34 L640 34 L640 90 Z" fill="var(--brand-green)"/>
    <path d="M0 72 L640 54 L640 90 L0 90 Z" fill="var(--paper)"/>
    <path d="M0 78 L640 60 L640 90 L0 90 Z" fill="var(--brand-blue)"/>
  </svg>
</section>

</body>
</html>
```